Capability Statement Brochure - Corporate

We need to provide our corporate clients with an elegant, professional and well designed capability statement that not only details what our business can offer, but reflects our professionalism with relevant technical photos. I am thinking two pages A 4 pdf will be suitable if the text can fit without looking crowded but happy to extend to 3 or 4 pages if needed . Colours and details can be taken from our website www.quorintech.com.au Some photos have been attached however if we need more professional stock photos I am happy to use them if needed. This project needs to convince potential clients we are the best in industry and our capability is extensive. Please help us relay this to our customers. Thank you,.

Target Market(s)

Corporate, Government, Education, Defence, Healthcare

Industry/Entity Type

Audio Visual Integration

Colors
0054AA
0677BA
7BADD7
CADEEF
E8F1F8

Requirements
Must have
• Style, look classy, sophisticated and technical
Nice to have
• Quorin Tech colours, Logo, website and email and include the PRISM LED Logo
Should not have
• Messy, too much clutter, not easy to read.

```html
<!DOCTYPE html>
<html lang="en">
<head>
<meta charset="utf-8">
<title>Quorin Tech – Capability Statement</title>
<link href="https://fonts.googleapis.com/css2?family=Lato:wght@400;700&display=swap" rel="stylesheet">
<style>
  :root{
    --stage:#ebeef5;
    --paper:#ffffff;
    --band:#acd3f0;
    --panel:#dfeef9;
    --ink:#1c2b3a;
    --copy:#2e3a46;
    --brand:#0054aa;
    --brand-mid:#0677ba;
    --footer:#2c56a5;
    --accent:#e0642a;
  }
  *{box-sizing:border-box;margin:0;padding:0}
  html,body{width:1200px;height:530px;overflow:hidden;background:var(--stage);font-family:"Lato",Arial,sans-serif;color:var(--copy)}
  .page{position:absolute;top:33px;width:358px;height:463px;background:var(--paper);overflow:hidden;box-shadow:0 1px 3px rgba(0,0,0,.08)}
  .page-one{left:37px}.page-two{left:421px}.page-three{left:806px}
  .abs{position:absolute}
  .band{position:absolute;background:var(--band);height:20px;display:flex;align-items:center;padding-left:14px;font-size:8.6px;color:var(--ink)}
  .panel{position:absolute;background:var(--panel)}
  .panel-head{position:absolute;left:14px;font-size:8.6px;line-height:10.5px;color:var(--ink)}
  .copy{position:absolute;font-size:4.7px;line-height:8.2px;color:var(--copy)}
  .copy p+p{margin-top:4px}
  .photo{position:absolute}
  .bullets{position:absolute;list-style:none;font-size:4.7px;line-height:10.5px;color:var(--copy)}
  .bullets li{position:relative;padding-left:8px}
  .bullets li::before{content:"";position:absolute;left:0;top:4px;width:2.6px;height:2.6px;background:var(--brand)}
  /* page one */
  .brand-name{position:absolute;left:0;right:0;top:11px;text-align:center;font-size:7px;color:var(--brand)}
  .brand-name .mark{display:inline-block;width:7px;height:7px;background:var(--brand);margin-right:4px;vertical-align:-1px}
  .hero{left:0;top:32px;width:358px;height:92px;background:linear-gradient(180deg,#3c5a86 0%,#243a5c 60%,#1a2a44 100%)}
  .hero-title{position:absolute;left:0;right:0;top:68px;text-align:center;color:#fff;font-size:11px}
  .hero-rule{position:absolute;left:168px;top:84px;width:22px;height:1px;background:var(--accent)}
  /* markets */
  .market{position:absolute;top:175px;width:44.5px;height:44px;border:1px solid var(--band);display:flex;flex-direction:column;align-items:center;padding-top:7px}
  .market svg{width:12px;height:12px}
  .market span{font-size:4.5px;line-height:6px;text-align:center;margin-top:4px;color:var(--copy)}
  /* footer */
  .contact-bar{position:absolute;left:0;bottom:0;width:358px;height:36px;background:var(--footer);color:#fff;font-size:6.2px;display:flex;align-items:center;justify-content:space-between;padding:0 14px 0 16px}
  .contact-bar span{display:flex;align-items:center;gap:4px}
  .contact-bar svg{width:9px;height:9px}
</style>
</head>
<body>

<section class="page page-one">
  <div class="brand-name"><span class="mark"></span>quorin tech</div>
  <div class="photo hero" role="img" aria-label="Boardroom with rows of black office chairs, tinted blue"></div>
  <div class="hero-title">Capability Statement</div>
  <div class="hero-rule"></div>

  <div class="band" style="top:124px;left:0;width:358px">Company Overview</div>
  <div class="copy" style="left:14px;top:150px;width:168px">
    <p>Quorin Tech (QT) is a leading Australian audiovisual integration specialist delivering advanced AV, unified communications, collaboration environments, and large‑scale digital display systems across Australia.</p>
    <p>With more than 26 years of industry experience, QT provides end‑to‑end services including system design, engineering, installation, commissioning, and long‑term technical support. Our solutions enable organisations to communicate, collaborate, and share information effectively across boardrooms, control centres, training environments, operational facilities, and large public spaces.</p>
    <p>QT works across a broad range of sectors including healthcare, corporate enterprise, government, defence, mining and resources, and education. Our team combines deep technical expertise with a strong understanding of operational environments where reliability, security, and ease of use are essential.</p>
  </div>
  <div class="photo" style="left:197px;top:152px;width:147px;height:130px;background:linear-gradient(160deg,#9aa0a8 0%,#6b6f86 45%,#3d4266 100%)" role="img" aria-label="Tiered lecture theatre with blue seating and a lectern monitor in the foreground"></div>

  <div class="band" style="top:290px;left:0;width:358px">Core Capabilities</div>
  <ul class="bullets" style="left:22px;top:321px">
    <li>AV System Design and Engineering</li>
    <li>Unified Communications and Collaboration Systems</li>
    <li>LED Video Walls and Large Format Displays</li>
    <li>Control Rooms and Operations Centres</li>
    <li>Boardrooms and Executive Meeting Spaces</li>
  </ul>
  <ul class="bullets" style="left:184px;top:321px">
    <li>Education and Training Environments</li>
    <li>Digital Signage and Information Display Networks</li>
    <li>AV over IP and Networked Media Systems</li>
    <li>System Programming, Automation and Control</li>
    <li>Ongoing Service, Maintenance and Technical Support</li>
  </ul>
  <div class="photo" style="left:0;top:391px;width:358px;height:72px;background:linear-gradient(135deg,#3a2a22 0%,#1c1c1e 40%,#2a2c30 100%)" role="img" aria-label="Hand adjusting faders on an audio mixing console"></div>
</section>

<section class="page page-two">
  <div class="band" style="top:14px;left:0;width:358px">LED Video Wall Expertise</div>
  <div class="copy" style="left:14px;top:43px;width:165px">
    <p>Quorin Tech has extensive experience designing and installing direct‑view LED video walls for corporate environments, education facilities, public venues, and large presentation spaces.</p>
    <p>Our proprietary PRISM LED video wall solutions provide exceptional brightness, durability, and reliability for high‑impact display environments such as school halls, gymnasiums, corporate auditoriums, and public venues.</p>
    <p>QT provides complete LED video wall solutions including structural design, engineering certification, installation, commissioning, and ongoing support.</p>
  </div>
  <div class="photo" style="left:197px;top:44px;width:147px;height:84px;background:linear-gradient(160deg,#b7a98c 0%,#7d715e 50%,#3e3a34 100%)" role="img" aria-label="Meeting room with a large LED video wall showing the product name"></div>

  <div class="band" style="top:142px;left:0;width:358px">Markets Served</div>

  <div class="market" style="left:14px"><svg viewBox="0 0 24 24"><path fill="#1e5fb0" d="M12 21s-8-5.2-8-11a4.5 4.5 0 0 1 8-2.8A4.5 4.5 0 0 1 20 10c0 5.8-8 11-8 11z"/><path stroke="#fff" stroke-width="2" d="M12 9v6M9 12h6"/></svg><span>Healthcare</span></div>
  <div class="market" style="left:61.5px"><svg viewBox="0 0 24 24"><rect x="3" y="7" width="18" height="13" rx="1.5" fill="#1e5fb0"/><rect x="9" y="4" width="6" height="4" fill="none" stroke="#1e5fb0" stroke-width="1.8"/><path stroke="#fff" stroke-width="1.5" d="M3 12h18"/></svg><span>Corporate &amp;<br>Enterprise</span></div>
  <div class="market" style="left:109px"><svg viewBox="0 0 24 24"><path fill="#1e5fb0" d="M12 3l9 4.5H3z"/><rect x="3" y="19" width="18" height="2" fill="#1e5fb0"/><g fill="#1e5fb0"><rect x="5" y="9" width="2.5" height="9"/><rect x="10.7" y="9" width="2.5" height="9"/><rect x="16.5" y="9" width="2.5" height="9"/></g></svg><span>Government</span></div>
  <div class="market" style="left:156.5px"><svg viewBox="0 0 24 24"><path fill="#1e5fb0" d="M12 2l8 3v6c0 5-3.5 9-8 11-4.5-2-8-6-8-11V5z"/><path fill="#fff" d="M12 5v14c3-1.6 5-4.5 5-8V7z" opacity=".35"/></svg><span>Defence</span></div>
  <div class="market" style="left:204px"><svg viewBox="0 0 24 24"><path stroke="#1e5fb0" stroke-width="2.2" stroke-linecap="round" d="M5 21L15 9"/><path fill="none" stroke="#1e5fb0" stroke-width="2.2" d="M9 5c4-2 8-1 11 3"/></svg><span>Mining &amp;<br>Resources</span></div>
  <div class="market" style="left:251.5px"><svg viewBox="0 0 24 24"><path fill="#1e5fb0" d="M12 4l11 5-11 5L1 9z"/><path fill="#1e5fb0" d="M6 12v4c2 2 10 2 12 0v-4l-6 3z"/><path stroke="#1e5fb0" stroke-width="1.4" d="M21 10v6"/></svg><span>Education</span></div>
  <div class="market" style="left:299px"><svg viewBox="0 0 24 24"><g fill="#1e5fb0"><circle cx="7" cy="5" r="2.3"/><circle cx="17" cy="5" r="2.3"/><rect x="5" y="8.5" width="4" height="12" rx="1"/><rect x="15" y="8.5" width="4" height="12" rx="1"/><rect x="9" y="11" width="6" height="2"/></g></svg><span>Public Venues<br>&amp; Event Spaces</span></div>

  <div class="band" style="top:232px;left:0;width:175px;height:21px">Healthcare Experience</div>
  <div class="copy" style="left:14px;top:258px;width:162px">
    <p>QT has extensive experience delivering audiovisual solutions within major healthcare environments including clinical communication systems, specialist consultation rooms, training facilities, and hospital‑wide digital signage networks.</p>
    <p>For over 20 years QT has supported Westgate General Hospital with the design, implementation, and support of audiovisual infrastructure across departments including ICU, Emergency, Cardiology, Radiology, and Allied Health.</p>
  </div>

  <div class="panel" style="left:183px;top:232px;width:175px;height:99px">
    <div class="panel-head" style="top:6px">Corporate &amp;<br>Enterprise</div>
    <div class="copy" style="left:12px;top:28px;width:155px">
      <p>QT delivers modern collaboration environments that enable organisations to connect teams across offices, remote staff, and global partners.</p>
      <p>Solutions include boardrooms, hybrid meeting rooms, training facilities, corporate digital signage networks, and executive collaboration spaces.</p>
    </div>
  </div>

  <div class="panel" style="left:0;top:345px;width:175px;height:80px">
    <div class="panel-head" style="top:6px">Government &amp;<br>Defence</div>
    <div class="copy" style="left:14px;top:28px;width:152px">
      <p>QT supports government departments and defence organisations with reliable and secure audiovisual systems designed for operational environments including command centres, training facilities, situation rooms, and secure conferencing spaces.</p>
    </div>
  </div>

  <div class="band" style="top:345px;left:183px;width:175px;padding-left:12px">Mining &amp; Resources</div>
  <div class="copy" style="left:195px;top:369px;width:155px">
    <p>QT provides robust AV systems designed for industrial and remote environments including operations centres, training rooms, induction facilities, and remote collaboration systems supporting mining and energy sector operations.</p>
  </div>
</section>

<section class="page page-three">
  <div class="band" style="top:14px;left:0;width:175px;height:21px">Design &amp; Engineering</div>
  <div class="copy" style="left:14px;top:41px;width:160px">
    <p>QT provides comprehensive in‑house design and engineering services including system architecture, documentation, schematics, networked AV design, and integration with existing IT infrastructure.</p>
    <p>Our team works closely with architects, consultants, builders, and project managers to ensure seamless integration of audiovisual technology within new builds and refurbishment projects.</p>
  </div>

  <div class="panel" style="left:183px;top:14px;width:175px;height:80px">
    <div class="panel-head" style="top:6px;left:12px">Education</div>
    <div class="copy" style="left:12px;top:18px;width:158px">
      <p>QT delivers innovative AV solutions for schools, universities, and training institutions including lecture theatres, classrooms, hybrid learning environments, school halls, gymnasiums, and large‑scale LED display systems.</p>
    </div>
  </div>

  <div class="panel" style="left:0;top:108px;width:175px;height:94px">
    <div class="panel-head" style="top:6px">Implementation &amp;<br>Commissioning</div>
    <div class="copy" style="left:14px;top:28px;width:155px">
      <p>QT delivers complete turnkey project implementation including equipment procurement, professional installation, system configuration, testing, commissioning, and user training.</p>
      <p>Our accredited technicians ensure systems are delivered safely, efficiently, and with minimal disruption to operational environments.</p>
    </div>
  </div>

  <div class="band" style="top:108px;left:183px;width:175px;padding-left:12px">Service &amp; Support</div>
  <div class="copy" style="left:195px;top:132px;width:158px">
    <p>QT provides comprehensive ongoing support services including preventative maintenance, priority service response, remote diagnostics, system upgrades, and technology lifecycle planning.</p>
    <p>Our long‑term support partnerships ensure systems remain reliable, secure, and aligned with evolving organisational needs.</p>
  </div>

  <div class="band" style="top:215px;left:0;width:358px">Governance, Safety &amp; Compliance</div>
  <div class="copy" style="left:14px;top:263px;width:165px">
    <p>QT operates under strict safety and governance frameworks including OH&amp;S compliant work practices, industry‑certified technicians, and full public liability and professional indemnity coverage.</p>
    <p>Safety, compliance, and quality assurance are embedded throughout all project delivery activities.</p>
  </div>
  <div class="photo" style="left:197px;top:246px;width:147px;height:83px;background:linear-gradient(160deg,#e9ebec 0%,#c8cdd0 55%,#6d7478 100%)" role="img" aria-label="Bright meeting room with a white table, black chairs, wall display and potted plant"></div>

  <div class="band" style="top:339px;left:0;width:358px">Why Choose Quorin Tech</div>
  <ul class="bullets" style="left:21px;top:370px">
    <li>26+ years audiovisual integration experience</li>
    <li>Proven track record across multiple industries</li>
    <li>In‑house design and engineering capability</li>
  </ul>
  <ul class="bullets" style="left:183px;top:370px">
    <li>National project delivery capability</li>
    <li>LED video wall specialists</li>
    <li>Long‑term service and support partnerships</li>
  </ul>

  <footer class="contact-bar">
    <span><svg viewBox="0 0 24 24"><rect x="2" y="5" width="20" height="14" rx="1.5" fill="#fff"/><path d="M2.5 6l9.5 7 9.5-7" fill="none" stroke="#2c56a5" stroke-width="1.6"/></svg>dana@quorintech.com.au</span>
    <span><svg viewBox="0 0 24 24"><path fill="#fff" d="M6.6 10.8a15 15 0 0 0 6.6 6.6l2.2-2.2a1 1 0 0 1 1-.25 11 11 0 0 0 3.6.6 1 1 0 0 1 1 1V20a1 1 0 0 1-1 1A17 17 0 0 1 3 4a1 1 0 0 1 1-1h3.5a1 1 0 0 1 1 1 11 11 0 0 0 .6 3.6 1 1 0 0 1-.25 1z"/></svg>1300 555 017</span>
    <span><svg viewBox="0 0 24 24" fill="none" stroke="#fff" stroke-width="1.6"><circle cx="12" cy="12" r="9"/><ellipse cx="12" cy="12" rx="4" ry="9"/><path d="M3 12h18M5 7h14M5 17h14"/></svg>quorintech.com.au</span>
  </footer>
</section>

</body>
</html>
```